Meridian Rest Supply Needs Business Card

Looking for a very nice looking business card. Creative but not extravagant. We sell beds and pillows across the U.S. and need something professional but catchy. I have attached the logo.

Name : Dale Fenwick
Title : President
Phone : (800) 417-2964
Email: sleep@quorvana.com
Website: www.quorvana.com

Can be single-sided or double-sided
horizontal or vertical

Can use Blues/Greys

Target Market(s)

Mass Market

Industry/Entity Type

Retail

Contact Information for Business Card

Name : Dale Fenwick
Title : President
Phone : (800) 417-2964
Email: sleep@quorvana.com
Website: www.quorvana.com

Requirements
Must have
• Clean, Modern, Smooth
• Can use Blues/Greys
• On the other side without the information - have something simple like www.quorvana.com or our logo
Nice to have
• Surprise me
Should not have
• Nothing crazy, nothing cluttered

```html
<!DOCTYPE html>
<html lang="en">
<head>
<meta charset="utf-8">
<title>Meridian Rest Supply – Business Card</title>
<link href="https://fonts.googleapis.com/css2?family=Raleway:wght@300;400;700&display=swap" rel="stylesheet">
<style>
  :root {
    --backdrop: #e9ecef;
    --card: #ffffff;
    --brand-blue: #2fa6da;
    --brand-grey: #666666;
    --text-grey: #6f6f6f;
    --ghost-grey: #eeeeee;
  }
  * { margin: 0; padding: 0; box-sizing: border-box; }
  html, body {
    width: 1200px; height: 863px; overflow: hidden;
    background: var(--backdrop);
    font-family: "Raleway", sans-serif;
  }
  .stage {
    position: relative; width: 1200px; height: 863px;
    display: flex; justify-content: center; align-items: center; gap: 80px;
  }
  .card {
    position: relative; width: 340px; height: 595px;
    background: var(--card); overflow: hidden;
    box-shadow: 0 8px 24px rgba(0,0,0,0.12);
  }
  .card__shapes { position: absolute; inset: 0; }
  .shape--grey { fill: var(--brand-grey); }
  .shape--blue { fill: var(--brand-blue); }

  .front__wordmark {
    position: absolute; left: 0; right: 0; top: 238px;
    text-align: center;
    font-weight: 300; font-size: 40px; letter-spacing: 1px;
    color: var(--brand-blue);
  }

  .back__ghost {
    position: absolute; top: 40px; left: 250px;
    transform-origin: top left; transform: rotate(90deg) translateY(-100%);
    translate: 0 0;
    font-weight: 300; font-size: 110px; letter-spacing: 6px;
    color: var(--ghost-grey); white-space: nowrap; line-height: 1;
  }
  .back__marker {
    position: absolute; left: 0; top: 172px; width: 30px; height: 14px;
    background: var(--brand-grey);
  }
  .back__identity { position: absolute; left: 42px; top: 162px; }
  .back__name { font-weight: 700; font-size: 24px; color: var(--brand-blue); }
  .back__title { font-weight: 400; font-size: 17px; color: var(--text-grey); margin-top: 2px; }

  .contact-list {
    position: absolute; left: 30px; bottom: 48px; list-style: none;
  }
  .contact-list__item {
    display: flex; align-items: center; gap: 14px;
    font-size: 15px; color: var(--text-grey); margin-top: 10px;
  }
  .contact-list__icon { width: 20px; height: 20px; flex: none; }
  .contact-list__icon circle { fill: var(--brand-blue); }
  .contact-list__icon .glyph { fill: #fff; stroke: none; }
  .contact-list__icon .glyph-line { fill: none; stroke: #fff; stroke-width: 1.6; stroke-linecap: round; }
</style>
</head>
<body>
<main class="stage">

  <section class="card card--front" aria-label="Card front">
    <svg class="card__shapes" viewBox="0 0 340 595" aria-hidden="true">
      <polygon class="shape--grey" points="0,0 230,0 95,232 0,232"/>
      <polygon class="shape--blue" points="340,178 340,232 292,232"/>
      <rect class="shape--grey" x="0" y="298" width="44" height="10"/>
      <rect class="shape--blue" x="212" y="350" width="128" height="8"/>
      <rect class="shape--blue" x="200" y="364" width="140" height="4"/>
      <polygon class="shape--blue" points="70,595 340,595 340,372 232,372"/>
    </svg>
    <div class="front__wordmark">quorvana</div>
  </section>

  <section class="card card--back" aria-label="Card back">
    <div class="back__ghost" aria-hidden="true">quorvana</div>
    <div class="back__marker"></div>
    <div class="back__identity">
      <p class="back__name">Dale Fenwick</p>
      <p class="back__title">President</p>
    </div>
    <ul class="contact-list">
      <li class="contact-list__item">
        <svg class="contact-list__icon" viewBox="0 0 20 20" aria-hidden="true">
          <circle cx="10" cy="10" r="10"/>
          <path class="glyph" d="M5 8.5c0-1.5 2.3-2.5 5-2.5s5 1 5 2.5v.8h-2.6v-1H7.6v1H5z M6.5 10.5h7l1 3.5h-9z"/>
        </svg>
        <span>(800) 417-2964</span>
      </li>
      <li class="contact-list__item">
        <svg class="contact-list__icon" viewBox="0 0 20 20" aria-hidden="true">
          <circle cx="10" cy="10" r="10"/>
          <rect class="glyph" x="5" y="6.5" width="10" height="7" rx="1"/>
          <path class="glyph-line" d="M5.5 7.2 10 10.6l4.5-3.4" stroke="#2fa6da"/>
        </svg>
        <span>sleep@quorvana.com</span>
      </li>
      <li class="contact-list__item">
        <svg class="contact-list__icon" viewBox="0 0 20 20" aria-hidden="true">
          <circle cx="10" cy="10" r="10"/>
          <path class="glyph-line" d="M9 11a2.5 2.5 0 0 0 3.5 0l2-2a2.5 2.5 0 0 0-3.5-3.5l-.7.7 M11 9a2.5 2.5 0 0 0-3.5 0l-2 2a2.5 2.5 0 0 0 3.5 3.5l.7-.7"/>
        </svg>
        <span>www.quorvana.com</span>
      </li>
    </ul>
  </section>

</main>
</body>
</html>
```